Furniture restoration to chairs. Hand weaving.

Industry/Entity Type

Furniture

Contact Information for Business Card

The Wicker Loom
Cane, rush, splint and shaker tape.
482 Fenn Rd
Gull Cove
ME 04913
207 - 555 - 0183
Cell: 207 - 555 - 0276

For graphics I want a picture of a caned rocking chair or maybe a rush and a cane chair.

```html
<!DOCTYPE html>
<html lang="en">
<head>
<meta charset="utf-8">
<title>The Wicker Loom — Business Card</title>
<link href="https://fonts.googleapis.com/css2?family=Raleway:wght@400;500;600&family=Cormorant+SC:wght@600&display=swap" rel="stylesheet">
<style>
  :root {
    --navy: #0f1e40;
    --teal: #2bb3a3;
    --paper: #ffffff;
    --paper-shade: #eef0f3;
    --ink: #1a2440;
    --backdrop: #e4e1dc;
    --wood-dark: #3b2418;
    --wood-light: #7a5a3c;
  }
  * { margin: 0; padding: 0; box-sizing: border-box; }
  html, body { width: 1200px; height: 1000px; overflow: hidden; }
  body {
    background: var(--backdrop);
    font-family: "Raleway", Arial, sans-serif;
    position: relative;
  }
  .card {
    position: absolute;
    width: 540px;
    height: 310px;
    top: 345px;
    border-radius: 2px;
    overflow: hidden;
    box-shadow: 0 8px 24px rgba(0,0,0,0.22);
  }
  .card-front {
    left: 45px;
    background: radial-gradient(circle at 45% 35%, var(--paper) 55%, var(--paper-shade) 100%);
    color: var(--ink);
  }
  .card-back {
    left: 615px;
    background: var(--navy);
    color: #ffffff;
  }
  .wordmark {
    font-family: "Raleway", Arial, sans-serif;
    font-weight: 600;
    font-size: 34px;
    line-height: 0.95;
    letter-spacing: 0.5px;
    text-transform: uppercase;
  }
  .card-front .wordmark {
    position: absolute;
    left: 48px;
    top: 38px;
    color: var(--navy);
  }
  .chair-photo {
    position: absolute;
    left: 420px;
    top: 20px;
    width: 100px;
    height: 115px;
    background: linear-gradient(160deg, var(--wood-light), var(--wood-dark));
    border-radius: 4px;
  }
  .services {
    position: absolute;
    left: 320px;
    top: 140px;
    list-style: none;
    font-size: 14px;
    font-weight: 500;
    letter-spacing: 0.3px;
    line-height: 25px;
    text-transform: uppercase;
    color: var(--ink);
  }
  .services li::before {
    content: "•";
    font-size: 9px;
    margin-right: 9px;
    vertical-align: middle;
  }
  .owner-name {
    position: absolute;
    left: 48px;
    top: 205px;
    font-family: "Cormorant SC", Georgia, serif;
    font-weight: 600;
    font-size: 22px;
    letter-spacing: 0.5px;
    color: var(--navy);
  }
  .cell-line {
    position: absolute;
    left: 50px;
    top: 244px;
    font-size: 13px;
    font-weight: 500;
    color: var(--ink);
  }
  .front-band {
    position: absolute;
    left: 0;
    bottom: 0;
    width: 540px;
    height: 310px;
  }
  .card-back .wordmark {
    position: absolute;
    left: 0;
    right: 0;
    top: 82px;
    text-align: center;
    font-size: 40px;
    color: #ffffff;
  }
  .email-line {
    position: absolute;
    left: 0;
    right: 0;
    top: 232px;
    display: flex;
    justify-content: center;
    align-items: center;
    gap: 9px;
    font-size: 14px;
    color: #ffffff;
  }
</style>
</head>
<body>

  <section class="card card-front" aria-label="Business card front">
    <svg class="front-band" viewBox="0 0 540 310" aria-hidden="true">
      <path d="M0,292 C220,292 430,286 540,268 L540,310 L0,310 Z" fill="var(--navy)"/>
      <path d="M140,288 C320,287 460,278 540,254 L540,266 C440,284 320,290 140,290 Z" fill="var(--teal)"/>
    </svg>
    <div class="wordmark">The<br>Wicker<br>Loom</div>
    <div class="chair-photo" role="img" aria-label="Photo of a wooden rocking chair with a hand-caned seat and back"></div>
    <ul class="services">
      <li>Cane</li>
      <li>Rush</li>
      <li>Splint</li>
      <li>Shaker Tape</li>
      <li>Danish Cord</li>
    </ul>
    <div class="owner-name">Maren Thibodeau</div>
    <div class="cell-line">Cell: 207 - 555 - 0276</div>
  </section>

  <section class="card card-back" aria-label="Business card back">
    <div class="wordmark">The<br>Wicker<br>Loom</div>
    <div class="email-line">
      <svg width="14" height="11" viewBox="0 0 14 11" aria-hidden="true">
        <rect x="0.5" y="0.5" width="13" height="10" rx="1" fill="#ffffff"/>
        <path d="M1,1.5 L7,6 L13,1.5" fill="none" stroke="var(--navy)" stroke-width="1.2"/>
      </svg>
      <span>maren.thibodeau@wickerloom.com</span>
    </div>
  </section>

</body>
</html>
```